Bramblegate Card Company Business Cards

We are a trading card store with Zorvanix, sports and other TCG cards, we need a business card design that encompasses a clean cut, modern style with a retro flare. website is bramblegatecardco.example for reference. Can utilize a comic book era feel or a more modern outdoor feel to utilize the "Pacific Northwest" elements of tress, mountains, etc.

Industry/Entity Type

Trading cards and collectibles

Contact Information for Business Card

business name, email address, phone number, name, owner job title

Font styles to use
Sans Serif

```html
<!DOCTYPE html>
<html lang="en">
<head>
<meta charset="utf-8">
<title>Bramblegate Card Company – Business Cards</title>
<link href="https://fonts.googleapis.com/css2?family=Montserrat:wght@400;500;700;800&display=swap" rel="stylesheet">
<style>
  :root {
    --backdrop: #b9b9b9;
    --card-white: #ffffff;
    --card-grey: #737373;
    --brand-blue: #22bde0;
    --ink-dark: #3a3a3a;
    --logo-grey: #6f6f6f;
  }
  * { margin: 0; padding: 0; box-sizing: border-box; }
  html, body {
    width: 1200px; height: 815px; overflow: hidden;
    background: var(--backdrop);
    font-family: "Montserrat", Arial, sans-serif;
  }
  .card-pair {
    position: absolute; inset: 0;
    display: flex; align-items: center; justify-content: center; gap: 44px;
  }
  .card {
    width: 525px; height: 300px;
    border-radius: 22px;
    border-bottom: 5px solid var(--brand-blue);
    position: relative;
    overflow: hidden;
  }
  .card--front { background: var(--card-white); display: flex; }
  .card--back {
    background: var(--card-grey);
    display: flex; align-items: center; justify-content: center;
  }

  .front-brand {
    width: 46%;
    display: flex; align-items: center; justify-content: center;
    padding-left: 22px;
  }
  .divider {
    width: 2px; background: var(--brand-blue);
    margin: 70px 0 60px;
  }
  .front-details {
    flex: 1;
    padding: 46px 24px 0 28px;
    color: var(--ink-dark);
  }

  .wordmark {
    display: flex; align-items: center; gap: 12px;
  }
  .wordmark__dot {
    width: 18px; height: 18px; border-radius: 50%;
    background: var(--brand-blue); flex: none;
  }
  .wordmark__name {
    font-weight: 800; text-transform: uppercase;
    letter-spacing: 1px; line-height: 1.15;
  }
  .front-brand .wordmark__name { color: var(--logo-grey); font-size: 20px; }
  .card--back .wordmark__name { color: var(--card-white); font-size: 30px; }
  .card--back .wordmark__dot { width: 28px; height: 28px; }

  .person__name {
    color: var(--brand-blue); font-weight: 700;
    font-size: 24px; letter-spacing: 1px; text-transform: uppercase;
  }
  .person__title {
    font-size: 13px; font-weight: 500; letter-spacing: 0.5px;
    text-transform: uppercase; margin-top: 2px;
  }
  .address { font-size: 12.5px; line-height: 1.35; margin-top: 18px; }
  .contact-list { list-style: none; margin-top: 16px; font-size: 12.5px; }
  .contact-list li { display: flex; align-items: center; gap: 9px; line-height: 1.7; }
  .contact-list svg { width: 12px; height: 12px; flex: none; fill: var(--brand-blue); }
</style>
</head>
<body>
  <main class="card-pair">
    <section class="card card--front" aria-label="Business card front">
      <div class="front-brand">
        <div class="wordmark">
          <span class="wordmark__dot"></span>
          <span class="wordmark__name">Bramblegate<br>Card Company</span>
        </div>
      </div>
      <div class="divider"></div>
      <div class="front-details">
        <h1 class="person__name">Delan Harrow</h1>
        <p class="person__title">Manager</p>
        <p class="address">482 Fernhollow Road 27<br>Cedar Bend, WA 98011</p>
        <ul class="contact-list">
          <li>
            <svg viewBox="0 0 24 24" aria-hidden="true"><path d="M6.6 10.8a15.1 15.1 0 0 0 6.6 6.6l2.2-2.2a1 1 0 0 1 1-.25 11.4 11.4 0 0 0 3.6.57 1 1 0 0 1 1 1V20a1 1 0 0 1-1 1A17 17 0 0 1 3 4a1 1 0 0 1 1-1h3.5a1 1 0 0 1 1 1c0 1.25.2 2.45.57 3.57a1 1 0 0 1-.25 1z"/></svg>
            (555)014-2290
          </li>
          <li>
            <svg viewBox="0 0 24 24" aria-hidden="true"><path d="M2 5h20v14H2z M2 5l10 8 10-8" /></svg>
            hello@bramblegatecardco.example
          </li>
          <li>
            <svg viewBox="0 0 24 24" aria-hidden="true"><circle cx="12" cy="12" r="10"/></svg>
            www.bramblegatecardco.example
          </li>
        </ul>
      </div>
    </section>

    <section class="card card--back" aria-label="Business card back">
      <div class="wordmark">
        <span class="wordmark__dot"></span>
        <span class="wordmark__name">Bramblegate<br>Card Company</span>
      </div>
    </section>
  </main>
</body>
</html>
```